DESKHAVEN COWORKING Website design and coding

DESKHAVEN COWORKING

DESKHAVEN is Galveston’s first (and currently only) shared business co-working space. We share the same upscale, casual work environment, but we work independently on our own (or our team’s) projects and goals. For only a flat $195 membership fee per month, you have your very own all-inclusive, fun, personal business office environment. Website is written (Word file #12, below); and all pictures etc provided. Galveston is a beachy, coastal, historic city an hour from Houston, Texas USA. Logo (file 11 below) is temporary only.

Target Market(s)

Outside sales people, medical students looking for study hall, Houston companies looking for local office, real estate agents, graphic artists, entrepreneurs, etc

Contact Information for Business Card

will discuss --want to combine with current business card with multiple businesses

Logo Text

DESKHAVEN COWORKING

Coding

Coded - Design and coding required

Number of Pages Required

5+ page

Colors
ec1f27
fbed22

Requirements
Nice to have
• maroon/wine dominant with yellow and red accents, gray base are the colors of the space--website could coordinate--but open to creative ideas/combinations

```html
<!DOCTYPE html>
<html lang="en">
<head>
<meta charset="utf-8">
<title>DESKHAVEN COWORKING</title>
<link href="https://fonts.googleapis.com/css2?family=Oswald:wght@400;500;600&family=Lato:wght@400;700&family=Montserrat:wght@500&display=swap" rel="stylesheet">
<style>
:root{
  --red:#ec1f27;
  --yellow:#fbed22;
  --wine:#2e1118;
  --wine-deep:#1f0b10;
  --gray-base:#efefef;
  --ink:#222;
  --muted:#555;
  --footer:#151515;
  --white:#fff;
}
*{box-sizing:border-box;margin:0;padding:0}
html,body{width:1200px;height:5119px;overflow:hidden}
body{position:relative;font-family:'Lato',sans-serif;color:var(--ink);background:var(--white)}
.abs{position:absolute}
.heading{font-family:'Oswald',sans-serif;font-weight:500;letter-spacing:3px;text-transform:uppercase}
.pill{position:absolute;display:flex;align-items:center;justify-content:center;border-radius:20px;background:var(--red);color:var(--white);font-size:13px}
.photo{position:absolute}

/* hero */
.hero{position:absolute;left:0;top:0;width:1200px;height:715px;background:linear-gradient(180deg,#8a9099 0%,#6a6660 38%,#4a4440 60%,#2f2d2c 100%)}
.hero-shade{position:absolute;inset:0;background:rgba(20,15,15,.35)}
.brand{position:absolute;left:70px;top:112px;display:flex;align-items:center;gap:8px;color:var(--red);font-weight:700;font-size:15px}
.brand-mark{width:14px;height:14px;background:var(--yellow)}
.call{position:absolute;left:826px;top:26px;display:flex;align-items:center;gap:8px;color:var(--white);font-size:11px;line-height:13px}
.call-icon{width:32px;height:32px;border-radius:50%;background:var(--yellow);display:flex;align-items:center;justify-content:center}
.book{left:982px;top:24px;width:142px;height:32px;font-size:13px}
.nav{position:absolute;top:78px;left:0;width:1200px}
.nav a{position:absolute;color:var(--white);font-size:13px;text-decoration:none}
.nav a.active{color:var(--yellow)}
.nav a.active::after{content:"";position:absolute;left:0;right:0;top:22px;height:2px;background:var(--yellow)}
.hero-title{position:absolute;left:0;width:1200px;top:320px;text-align:center;color:var(--white);font-family:'Oswald',sans-serif;font-size:26px;letter-spacing:7px;line-height:36px}
.slide-dots{position:absolute;left:26px;top:350px;display:flex;align-items:center;gap:6px;color:var(--yellow);font-size:13px}
.slide-dots i{display:block;width:5px;height:5px;border-radius:50%;background:var(--yellow)}
.slide-dots b{display:block;width:18px;height:2px;background:var(--yellow)}

/* philosophy */
.philosophy{position:absolute;left:0;top:715px;width:1200px;height:795px;background:var(--wine)}
.section-title{position:absolute;left:0;width:1200px;text-align:center;font-size:26px}
.philosophy .section-title{top:68px;color:var(--white)}
.card{position:absolute;width:516px;height:255px;background:var(--white)}
.card .photo{left:0;top:0;width:259px;height:255px}
.card-body{position:absolute;left:285px;top:26px;width:216px}
.card-body h3{font-family:'Oswald',sans-serif;font-weight:500;font-size:14px;letter-spacing:1.5px;line-height:20px;text-transform:uppercase;color:var(--ink)}
.card-body p{font-size:10.5px;line-height:13.6px;color:#444;margin-top:10px}
.card .pill{left:285px;width:160px;height:32px;font-size:12px}

/* amenities */
.amenities{position:absolute;left:0;top:1510px;width:1200px;height:688px;background:var(--gray-base)}
.amenities .section-title{top:70px;color:var(--ink)}
.amen-intro{position:absolute;left:330px;width:600px;top:128px;text-align:center;font-size:12.5px;line-height:16px;color:#333}
.amenity{position:absolute;top:226px;width:240px;text-align:center}
.amenity .disc{width:198px;height:198px;border-radius:50%;margin:0 auto;display:flex;align-items:center;justify-content:center}
.amenity h4{font-family:'Montserrat',sans-serif;font-weight:500;font-size:16px;margin-top:34px;color:#222}
.amenity .go{margin:12px auto 0;width:18px;height:18px}

/* membership */
.membership{position:absolute;left:0;top:2198px;width:1200px;height:652px;background:linear-gradient(90deg,#3a2a28 0%,#2c1e1d 40%,#3b2620 70%,#2a1a1c 100%)}
.membership-shade{position:absolute;inset:0;background:rgba(60,10,25,.45)}
.plan{position:absolute;left:364px;top:87px;width:451px;height:509px;background:var(--yellow);padding:8px}
.plan-inner{position:relative;width:100%;height:100%;background:linear-gradient(180deg,#e0262a,#d11f25);color:var(--white);text-align:center}
.plan h2{position:absolute;top:24px;left:0;width:100%;font-size:30px;letter-spacing:2px}
.plan-price{position:absolute;top:81px;left:0;width:100%;height:76px;background:var(--yellow);display:flex;align-items:center;justify-content:center;gap:10px;color:var(--red);font-size:23px}
.plan-price strong{font-family:'Oswald',sans-serif;font-weight:600;font-size:56px;line-height:1}
.plan-note{position:absolute;top:176px;left:40px;width:355px;font-size:13px;line-height:22px}
.plan-features{position:absolute;top:270px;left:0;width:100%;font-family:'Oswald',sans-serif;font-size:14px;letter-spacing:1px}
.plan-list{position:absolute;top:300px;left:0;width:100%;list-style:none;font-size:13.5px;line-height:22.5px}
.plan-list li{display:flex;justify-content:center;align-items:center;gap:6px}
.plan-list li span.tick{display:inline-block;width:15px;height:15px}
.plan .pill{top:433px;width:160px;height:32px;background:var(--yellow);color:var(--red)}

/* picture */
.gallery{position:absolute;left:0;top:2850px;width:1200px;height:762px;background:var(--white)}
.gallery .section-title{top:74px;color:var(--ink)}

/* about */
.about{position:absolute;left:0;top:3612px;width:1200px;height:630px;background:var(--gray-base)}
.about .section-title{top:72px;color:var(--ink)}
.rule{position:absolute;left:575px;top:124px;width:50px;height:4px;background:var(--red)}
.square{position:absolute;background:var(--yellow)}
.about-copy{position:absolute;left:741px;top:204px;width:345px}
.about-copy h3{font-size:24px;letter-spacing:1.5px;color:#222}
.about-copy p{font-size:12.5px;line-height:17.5px;color:#555;margin-top:20px}

/* contact */
.contact{position:absolute;left:0;top:4242px;width:1200px;height:467px}
.contact-side{position:absolute;left:0;top:0;width:598px;height:467px;background:var(--wine)}
.contact-side h2{position:absolute;left:74px;top:68px;color:var(--white);font-size:27px;letter-spacing:2px}
.field{position:absolute;border:1px solid #bfb3b5;color:var(--white);font-size:11px;padding:0 12px;display:flex;align-items:center}
.field.area{align-items:flex-start;padding-top:12px}

/* footer */
.footer{position:absolute;left:0;top:4709px;width:1200px;height:328px;background:var(--footer);color:#ddd}
.footer-brand{position:absolute;left:78px;top:222px;display:flex;align-items:center;gap:10px;color:var(--red);font-size:22px;font-weight:700;letter-spacing:.5px}
.footer-brand span.mark{width:18px;height:18px;background:var(--yellow)}
.foot-col{position:absolute;top:72px}
.foot-col h5{font-family:'Oswald',sans-serif;font-weight:500;font-size:13px;letter-spacing:1.5px;color:var(--white)}
.foot-links{list-style:none;margin-top:30px;font-size:12.5px;line-height:22.8px}
.foot-links li::before{content:"•";margin-right:10px;color:#ddd}
.foot-links li.current{color:var(--yellow)}
.foot-line{display:flex;gap:12px;font-size:12.5px;line-height:25px}
.foot-line svg{flex:none;margin-top:6px}
.social{position:absolute;top:212px;display:flex;gap:16px}
.social i{display:block;width:32px;height:32px;border-radius:50%;background:#3a3a3a}
.social i.first{background:var(--red)}

.legal{position:absolute;left:0;top:5037px;width:1200px;height:82px;background:#f4f4f4}
.legal p{position:absolute;left:75px;top:38px;font-size:11.5px;color:#555}
.cards{position:absolute;left:962px;top:32px;display:flex;gap:8px}
.cards i{display:block;width:34px;height:26px;border-radius:3px}
</style>
</head>
<body>

<header class="hero">
  <div class="photo" role="img" aria-label="Photo of the coworking building on a street corner under a cloudy sky" style="inset:0;background:linear-gradient(180deg,#9aa3ae 0%,#7b7d7c 35%,#4f4a45 62%,#2c2b2a 100%)"></div>
  <div class="hero-shade"></div>
  <div class="brand"><span class="brand-mark"></span>DESKHAVEN COWORKING</div>
  <div class="call">
    <span class="call-icon"><svg width="14" height="14" viewBox="0 0 24 24"><path d="M6.6 10.8a15 15 0 0 0 6.6 6.6l2.2-2.2c.3-.3.7-.4 1-.2 1.1.4 2.3.6 3.6.6.6 0 1 .4 1 1V20c0 .6-.4 1-1 1A17 17 0 0 1 3 4c0-.6.4-1 1-1h3.5c.6 0 1 .4 1 1 0 1.3.2 2.5.6 3.6.1.3 0 .7-.2 1z" fill="#2e1118"/></svg></span>
    <span>Call us<br>555 010 2040</span>
  </div>
  <div class="pill book">Book Now</div>
  <nav class="nav">
    <a class="active" style="left:441px">Home</a>
    <a style="left:515px">The Deskhaven Philosophy</a>
    <a style="left:701px">Amenities</a>
    <a style="left:799px">Membership</a>
    <a style="left:914px">Picture</a>
    <a style="left:994px">About</a>
    <a style="left:1069px">Contact</a>
  </nav>
  <div class="slide-dots"><i></i><b></b><span>02</span></div>
  <h1 class="hero-title">CO-WORKING SPACE<br>FOR A SUCCESS</h1>
  <svg class="abs" style="left:590px;top:668px" width="20" height="40" viewBox="0 0 20 40"><line x1="10" y1="0" x2="10" y2="36" stroke="#fff" stroke-width="2"/><path d="M4 30 L10 37 L16 30" fill="none" stroke="#fff" stroke-width="2"/></svg>
</header>

<section class="philosophy">
  <h2 class="section-title heading">The Deskhaven Philosophy</h2>

  <article class="card" style="left:75px;top:143px">
    <div class="photo" role="img" aria-label="Photo of a lounge with sofas and a cubby shelf" style="background:linear-gradient(160deg,#d8d2c2,#8d7a55 55%,#3c3530)"></div>
    <div class="card-body">
      <h3>Work outside the home</h3>
      <p>Free yourself for the burdens of house or school, and work in an environment that MOTIVATES you instead of DISTRACTS you. Meet like-minded people that can help you along, and yet you have the option to work in a quiet - and very comfortable - private office cubicle.</p>
    </div>
    <div class="pill" style="top:197px">Read More</div>
  </article>

  <article class="card" style="left:608px;top:143px">
    <div class="photo" role="img" aria-label="Photo of a bar table with stools under pendant lamps" style="background:linear-gradient(160deg,#c9b98a,#8a6a3a 55%,#3a2a22)"></div>
    <div class="card-body">
      <h3>Deskhaven the competition</h3>
      <p>Because of the flexibility, prestigious location, opportunities to meet and network with active professionals, and the available tech and amenities, you have all the tools you need to excel in your chosen field.</p>
    </div>
    <div class="pill" style="top:197px">Read More</div>
  </article>

  <article class="card" style="left:75px;top:420px">
    <div class="photo" role="img" aria-label="Photo of the shared kitchen with dark cabinets" style="background:linear-gradient(160deg,#bdb2a0,#5a3b35 55%,#2a1d1c)"></div>
    <div class="card-body">
      <h3>Work it out with your coworkers</h3>
      <p>DESKHAVEN is a community – if you are making a pot of (free) coffee – ask and make enough for everyone that wants some! You rapidly become part of more than an office – you have new friends, teachers, people you can trade skills and your experience with!</p>
    </div>
    <div class="pill" style="top:200px">Read More</div>
  </article>

  <article class="card" style="left:608px;top:420px">
    <div class="photo" role="img" aria-label="Photo of the kitchen with a steel fridge and counter" style="background:linear-gradient(160deg,#c8c0b0,#6b4a3c 55%,#2a1f1d)"></div>
    <div class="card-body">
      <h3>Work out the path to your success</h3>
      <p>As your business grows, there are other beautiful, "dedicated desk" private executive offices, and full office suites available in the building. Meet your coworkers and synergize with their energy and experience to jump-start your own career.</p>
    </div>
    <div class="pill" style="top:195px">Read More</div>
  </article>
</section>

<section class="amenities">
  <h2 class="section-title heading">Amenities</h2>
  <p class="amen-intro">DESKHAVEN is the first Galveston co-working space, and offers all of the following features, all included in your monthly $195 membership fee</p>

  <div class="amenity" style="left:91px">
    <div class="disc" style="background:var(--red)">
      <svg width="104" height="104" viewBox="0 0 104 104" fill="none" stroke="#fff" stroke-width="3"><rect x="18" y="24" width="68" height="30"/><line x1="52" y1="24" x2="52" y2="54"/><rect x="38" y="34" width="28" height="24"/><line x1="52" y1="58" x2="52" y2="72"/><line x1="40" y1="72" x2="64" y2="72"/><line x1="18" y1="54" x2="18" y2="82"/><line x1="86" y1="54" x2="86" y2="82"/></svg>
    </div>
    <h4>Private Cubicle</h4>
    <svg class="go" viewBox="0 0 18 18"><circle cx="9" cy="9" r="8" fill="none" stroke="#555"/><path d="M5 9h8M10 6l3 3-3 3" fill="none" stroke="#555"/></svg>
  </div>

  <div class="amenity" style="left:351px">
    <div class="disc" style="background:var(--yellow)">
      <svg width="104" height="104" viewBox="0 0 104 104" fill="none" stroke="#2e1118" stroke-width="3"><rect x="20" y="52" width="64" height="26" rx="3"/><line x1="36" y1="52" x2="36" y2="30"/><line x1="68" y1="52" x2="68" y2="30"/><path d="M40 40a17 17 0 0 1 24 0M45 45a10 10 0 0 1 14 0"/><circle cx="52" cy="50" r="1.5" fill="#2e1118"/><circle cx="30" cy="65" r="1.5" fill="#2e1118"/><circle cx="36" cy="65" r="1.5" fill="#2e1118"/><rect x="62" y="61" width="14" height="8"/></svg>
    </div>
    <h4>Free Wifi</h4>
    <svg class="go" viewBox="0 0 18 18"><circle cx="9" cy="9" r="8" fill="none" stroke="#555"/><path d="M5 9h8M10 6l3 3-3 3" fill="none" stroke="#555"/></svg>
  </div>

  <div class="amenity" style="left:611px">
    <div class="disc" style="background:var(--red)">
      <svg width="104" height="104" viewBox="0 0 104 104" fill="none" stroke="#fff" stroke-width="3"><path d="M78 46a28 28 0 1 0-6 22"/><path d="M74 36l5 9 8-6"/><path d="M50 30v20l10 6"/><text x="54" y="76" fill="#fff" stroke="none" font-family="Lato,sans-serif" font-size="28">24</text></svg>
    </div>
    <h4>24 hour access.</h4>
    <svg class="go" viewBox="0 0 18 18"><circle cx="9" cy="9" r="8" fill="none" stroke="#555"/><path d="M5 9h8M10 6l3 3-3 3" fill="none" stroke="#555"/></svg>
  </div>

  <div class="amenity" style="left:868px">
    <div class="disc" style="background:var(--red)">
      <svg width="104" height="104" viewBox="0 0 104 104" fill="none" stroke="#fff" stroke-width="3"><path d="M16 48 52 18l36 30"/><path d="M24 42v42h56V42"/><rect x="40" y="44" width="24" height="16"/><line x1="52" y1="60" x2="52" y2="66"/><line x1="32" y1="68" x2="72" y2="68"/><line x1="36" y1="68" x2="36" y2="84"/><line x1="68" y1="68" x2="68" y2="84"/></svg>
    </div>
    <h4>private office cubicles</h4>
    <svg class="go" viewBox="0 0 18 18"><circle cx="9" cy="9" r="8" fill="none" stroke="#555"/><path d="M5 9h8M10 6l3 3-3 3" fill="none" stroke="#555"/></svg>
  </div>

  <div class="pill" style="left:521px;top:565px;width:161px;height:32px">View More</div>
</section>

<section class="membership">
  <div class="photo" role="img" aria-label="Photo of the work room with chairs, sofas and pendant lamps" style="inset:0;background:linear-gradient(90deg,#5a4a40 0%,#3a2c28 40%,#4a3426 70%,#2d2020 100%)"></div>
  <div class="membership-shade"></div>
  <div class="plan">
    <div class="plan-inner">
      <h2 class="heading">Membership</h2>
      <div class="plan-price"><span>FOR ONLY</span><strong>$195</strong><span>A MONTH</span></div>
      <p class="plan-note">charged to your credit card, you get the all-inclusive amenities listed above, for one flat fee. The only "extras" are for copies, on a per-copy basis</p>
      <div class="plan-features">FEATURES</div>
      <ul class="plan-list">
        <li><span class="tick"><svg viewBox="0 0 15 15"><circle cx="7.5" cy="7.5" r="6.5" fill="none" stroke="#fbed22" stroke-width="1.5"/><path d="M4.5 7.5l2 2 4-4" fill="none" stroke="#fbed22" stroke-width="1.5"/></svg></span>WiFi</li>
        <li><span class="tick"><svg viewBox="0 0 15 15"><circle cx="7.5" cy="7.5" r="6.5" fill="none" stroke="#fbed22" stroke-width="1.5"/><path d="M4.5 7.5l2 2 4-4" fill="none" stroke="#fbed22" stroke-width="1.5"/></svg></span>Coffee</li>
        <li><span class="tick"><svg viewBox="0 0 15 15"><circle cx="7.5" cy="7.5" r="6.5" fill="none" stroke="#fbed22" stroke-width="1.5"/><path d="M4.5 7.5l2 2 4-4" fill="none" stroke="#fbed22" stroke-width="1.5"/></svg></span>Conference Room</li>
        <li><span class="tick"><svg viewBox="0 0 15 15"><circle cx="7.5" cy="7.5" r="6.5" fill="none" stroke="#fbed22" stroke-width="1.5"/><path d="M4.5 7.5l2 2 4-4" fill="none" stroke="#fbed22" stroke-width="1.5"/></svg></span>Office Use</li>
        <li><span class="tick"><svg viewBox="0 0 15 15"><circle cx="7.5" cy="7.5" r="6.5" fill="none" stroke="#fbed22" stroke-width="1.5"/><path d="M4.5 7.5l2 2 4-4" fill="none" stroke="#fbed22" stroke-width="1.5"/></svg></span>Use of The Kitchen</li>
      </ul>
      <div class="pill" style="left:59px">Read More</div>
      <div class="pill" style="left:234px">Buy Now</div>
    </div>
  </div>
</section>

<section class="gallery">
  <h2 class="section-title heading">Picture</h2>
  <div class="photo" role="img" aria-label="Photo of a hallway with a printer and office door" style="left:75px;top:140px;width:332px;height:213px;background:linear-gradient(150deg,#cfd3d6,#8c8f90 55%,#4a4444)"></div>
  <div class="photo" role="img" aria-label="Photo of the kitchen counter at night" style="left:427px;top:140px;width:340px;height:450px;background:linear-gradient(180deg,#3a3636,#1f1a1a 45%,#2a1216 100%)"></div>
  <svg class="abs" style="left:583px;top:353px" width="28" height="28" viewBox="0 0 28 28" fill="none" stroke="#fff" stroke-width="2"><path d="M2 9V2h7M19 2h7v7M26 19v7h-7M9 26H2v-7"/><rect x="9" y="9" width="10" height="10"/></svg>
  <div class="photo" role="img" aria-label="Photo of a potted plant on a counter" style="left:789px;top:140px;width:334px;height:213px;background:linear-gradient(150deg,#6a6460,#a08070 50%,#2e2222)"></div>
  <div class="photo" role="img" aria-label="Photo of a bar table with stools and pendant lamps" style="left:75px;top:377px;width:332px;height:213px;background:linear-gradient(150deg,#c2b48a,#7a5e3a 55%,#2e2420)"></div>
  <div class="photo" role="img" aria-label="Photo of a kitchen island with stools" style="left:789px;top:377px;width:334px;height:213px;background:linear-gradient(150deg,#b8b4ac,#5a2c2c 55%,#2a1e1c)"></div>
  <div class="pill" style="left:517px;top:643px;width:159px;height:34px">View More</div>
</section>

<section class="about">
  <h2 class="section-title heading">About Us</h2>
  <div class="rule"></div>
  <div class="photo" role="img" aria-label="Photo of the open work room with lamps and chairs" style="left:109px;top:120px;width:334px;height:266px;background:linear-gradient(160deg,#c8c4b8,#8a7450 50%,#3a2e26)"></div>
  <div class="photo" role="img" aria-label="Photo of a glass-walled room with sofas" style="left:264px;top:183px;width:437px;height:354px;background:linear-gradient(160deg,#9a9a94,#6a5a40 50%,#2e2822)"></div>
  <div class="square" style="left:459px;top:131px;width:38px;height:32px"></div>
  <div class="square" style="left:209px;top:366px;width:37px;height:34px"></div>
  <div class="about-copy">
    <h3 class="heading">Deskhaven Coworking</h3>
    <p>DESKHAVEN is Galveston's first (and currently only) shared business co-working space. We share the same upscale, casual work environment, but we work independently on our own (or our team's) projects and goals.</p>
    <p>For only a flat $195 membership fee per month, you have your very own all-inclusive, fun, personal business office environment.</p>
  </div>
  <div class="pill" style="left:737px;top:420px;width:159px;height:32px">Read More</div>
</section>

<section class="contact">
  <div class="contact-side">
    <h2 class="heading">Quick Contact</h2>
    <div class="field" style="left:75px;top:135px;width:229px;height:46px">Name*</div>
    <div class="field" style="left:318px;top:135px;width:228px;height:46px">Email*</div>
    <div class="field" style="left:75px;top:195px;width:229px;height:44px">Phone*</div>
    <div class="field" style="left:318px;top:195px;width:228px;height:44px">Your Business</div>
    <div class="field area" style="left:75px;top:251px;width:471px;height:113px">Message</div>
    <div class="pill" style="left:75px;top:382px;width:159px;height:32px">Send</div>
  </div>
  <div class="photo" role="img" aria-label="Photo of the work room with black chairs and a sofa" style="left:598px;top:0;width:602px;height:467px;background:linear-gradient(160deg,#b0aca0,#6a5a42 50%,#2a2420)"></div>
</section>

<footer class="footer">
  <div class="footer-brand"><span class="mark"></span>DESKHAVEN COWORKING</div>

  <div class="foot-col" style="left:417px">
    <h5>QUICK LINK</h5>
    <ul class="foot-links">
      <li class="current">Home</li><li>About</li><li>Amenities</li><li>Membership</li><li>Picture</li><li>Philosophy</li><li>Contact</li>
    </ul>
  </div>

  <div class="foot-col" style="left:590px">
    <h5>PHYSICAL LOCATION</h5>
    <div class="foot-line" style="margin-top:26px">
      <svg width="10" height="13" viewBox="0 0 10 13"><path d="M5 12S1 7.5 1 5a4 4 0 0 1 8 0c0 2.5-4 7-4 7z" fill="none" stroke="#ddd"/><circle cx="5" cy="5" r="1.5" fill="#ddd"/></svg>
      <span>Deskhaven Coworking<br>418 Seawall Row, Suite 12<br>Galveston, TX 77551</span>
    </div>
    <div class="foot-line" style="margin-top:18px">
      <svg width="12" height="10" viewBox="0 0 12 10"><rect x="1" y="3" width="10" height="6" fill="none" stroke="#ddd"/><path d="M2 3V1h8v2" fill="none" stroke="#ddd"/></svg>
      <span>555-014-3388</span>
    </div>
    <div class="foot-line">
      <svg width="12" height="9" viewBox="0 0 12 9"><rect x=".5" y=".5" width="11" height="8" fill="none" stroke="#ddd"/><path d="M1 1l5 4 5-4" fill="none" stroke="#ddd"/></svg>
      <span style="line-height:14px;margin-top:3px">hello@deskhavenmail.com</span>
    </div>
  </div>

  <div class="foot-col" style="left:848px">
    <h5>MAILING ADDRESS FOR MANAGEMENT</h5>
    <div class="foot-line" style="margin-top:26px">
      <svg width="10" height="13" viewBox="0 0 10 13"><path d="M5 12S1 7.5 1 5a4 4 0 0 1 8 0c0 2.5-4 7-4 7z" fill="none" stroke="#ddd"/><circle cx="5" cy="5" r="1.5" fill="#ddd"/></svg>
      <span>Harborline Holdings<br>77 Commerce Ave., Suite 500<br>Houston, TX 77010</span>
    </div>
  </div>

  <div class="social" style="left:848px"><i class="first"></i><i></i><i></i><i></i></div>
</footer>

<div class="legal">
  <p>Copyright © Deskhaven Coworking . All Rights Reserved</p>
  <div class="cards">
    <i style="background:#26408f"></i>
    <i style="background:#1b4fb3"></i>
    <i style="background:#e8e8e8;border:1px solid #ccc"></i>
    <i style="background:#2b7bd0"></i>
  </div>
</div>

</body>
</html>
```